We need a business card for a company which is just starting up. The company name is Lumencrest Executive Services and we do a variety of things such as: support services for executives/leaders, sales team creation/management/training, and implementation of new programs to enhance a company's culture. The final design should be simple, professional and create a buzz of wanting to learn more. The owner is a woman of power, poise and leadership while she maintains qualities of caring, compassionate and honest. Her clients respect and refer her constantly. The colors are up for negotiation but should capture strength and softness at the same time. Possible colors: chocolate brown, dark pink, periwinkle. See attachment.

Target Market(s)

Medium to Large Businesses

Industry/Entity Type

Leadership

Requirements
Nice to have
• Qr code

```html
<!DOCTYPE html>
<html lang="en">
<head>
<meta charset="utf-8">
<title>Lumencrest Executive Services – Business Card</title>
<link href="https://fonts.googleapis.com/css2?family=Courgette&display=swap" rel="stylesheet">
<style>
  :root {
    --page: #ffffff;
    --front-bg: #9b0552;
    --back-bg: #6a1e47;
    --vine-light: rgba(214, 178, 196, 0.85);
    --vine-soft: rgba(214, 178, 196, 0.25);
    --brand-dark: #111111;
    --brand-light: #c9a9ba;
    --name-pink: #e0a9c6;
    --detail: #d9bccb;
    --reflect: rgba(155, 5, 82, 0.10);
    --reflect-back: rgba(106, 30, 71, 0.10);
  }
  * { margin: 0; padding: 0; box-sizing: border-box; }
  html, body {
    width: 1200px;
    height: 543px;
    overflow: hidden;
    background: var(--page);
    font-family: "Courgette", cursive;
  }
  .canvas { position: relative; width: 1200px; height: 543px; }

  .card {
    position: absolute;
    top: 83px;
    width: 540px;
    height: 330px;
  }
  .card--front { left: 38px; background: var(--front-bg); }
  .card--back  { left: 622px; background: var(--back-bg); }

  .reflection {
    position: absolute;
    top: 413px;
    width: 540px;
    height: 50px;
  }
  .reflection--front { left: 38px; background: linear-gradient(var(--reflect), transparent); }
  .reflection--back  { left: 622px; background: linear-gradient(var(--reflect-back), transparent); }

  .vine {
    position: absolute;
    left: 0;
    top: 0;
    width: 70px;
    height: 100%;
    background: linear-gradient(90deg, var(--vine-light) 0%, var(--vine-soft) 70%, transparent 100%);
    opacity: 0.6;
  }

  .brand {
    position: absolute;
    color: var(--brand-dark);
    line-height: 1;
  }
  .brand__name { display: block; }
  .brand__tag  { display: block; }

  .card--front .brand { left: 140px; top: 130px; }
  .card--front .brand__name { font-size: 40px; }
  .card--front .brand__tag  { font-size: 19px; margin-top: 8px; padding-left: 4px; }

  .card--back .brand { left: 182px; top: 142px; color: var(--brand-light); }
  .card--back .brand__name { font-size: 27px; }
  .card--back .brand__tag  { font-size: 13px; margin-top: 5px; padding-left: 3px; }

  .owner {
    position: absolute;
    right: 128px;
    top: 233px;
    text-align: right;
    color: var(--name-pink);
  }
  .owner__name  { font-size: 19px; line-height: 1.2; }
  .owner__title { font-size: 13px; margin-top: 4px; }

  .contact {
    position: absolute;
    left: 216px;
    top: 232px;
    border-collapse: collapse;
    color: var(--detail);
    font-size: 10.5px;
  }
  .contact td { padding: 1px 0; line-height: 13px; }
  .contact__label { width: 52px; }
  .contact__sep { width: 26px; }
  .contact__value { text-align: left; }
</style>
</head>
<body>
  <main class="canvas">
    <section class="card card--front" aria-label="Card front">
      <div class="vine" role="img" aria-label="Climbing leaf vine ornament along the left edge"></div>
      <div class="brand">
        <span class="brand__name">Lumencrest</span>
        <span class="brand__tag">Executive Services</span>
      </div>
      <div class="owner">
        <p class="owner__name">Marissa Calloway</p>
        <p class="owner__title">Owner</p>
      </div>
    </section>
    <div class="reflection reflection--front"></div>

    <section class="card card--back" aria-label="Card back">
      <div class="vine" role="img" aria-label="Climbing leaf vine ornament along the left edge"></div>
      <div class="brand">
        <span class="brand__name">Lumencrest</span>
        <span class="brand__tag">Executive Services</span>
      </div>
      <table class="contact">
        <tr><td class="contact__label">Phone</td><td class="contact__sep">:</td><td class="contact__value">(555) 555-5555</td></tr>
        <tr><td class="contact__label">Email</td><td class="contact__sep">:</td><td class="contact__value">marissa@email.com</td></tr>
        <tr><td class="contact__label">Website</td><td class="contact__sep">:</td><td class="contact__value">www.website.com</td></tr>
      </table>
    </section>
    <div class="reflection reflection--back"></div>
  </main>
</body>
</html>
```